New business card for a regional office of a US M&A company

We need business card for a finance company, office based in Hong Kong , our Head office is in US, our business is to Merge and acquires companies , the new office will be a regional office for the Asia Pacific region. We want to use the head office logo as attached ( but don't have to be exactly the same, can be a variation to it) as a base and then add Asia Pacific alongside the logo.
We would prefer to have be bilingual Eng + Chinese, although we don't really have Chinese company name .

Industry/Entity Type

Business

Contact Information for Business Card

Carla Beth Soren
 

VP,
APAC M&A Operations
Tovar Crest Asia Pacific Limited
 
Unit 1407, K82
27 Sai Lok Fung Road, 
Hong Kong 
 
M: +852 6481 2037
T : +852 2736 4100
F : +852 2736 4155
VOIP: 4813
 
cbsoren@tovarcrest.com

Font styles to use
Serif
Sans Serif

Colors

Designer to choose colors to be used in the design.

Requirements
Must have
• APAC Office

```html
<!DOCTYPE html>
<html lang="en">
<head>
<meta charset="utf-8">
<title>Tovar Crest Asia Pacific – Business Card</title>
<link rel="stylesheet" href="https://fonts.googleapis.com/css2?family=Open+Sans:wght@400;600;700&display=swap">
<style>
  :root {
    --backdrop: #3a3a3c;
    --card: #1d1d1f;
    --brand-cyan: #22aed1;
    --stripe-light: #c9cbcd;
    --ink-white: #f2f2f2;
    --emboss: #4a4a4d;
    --mark-silver: #d9d9db;
  }
  * { margin: 0; padding: 0; box-sizing: border-box; }
  html, body { width: 799px; height: 1200px; overflow: hidden; }
  body {
    background: var(--backdrop);
    font-family: "Open Sans", sans-serif;
    position: relative;
  }
  .card {
    position: absolute;
    left: 90px;
    width: 620px;
    height: 354px;
    background: var(--card);
    border-radius: 3px;
    box-shadow: 0 6px 18px rgba(0,0,0,0.35);
    overflow: hidden;
  }
  .card--front { top: 110px; }
  .card--back { top: 730px; }

  /* Front */
  .front-brand {
    position: absolute;
    left: 0; right: 0; top: 130px;
    display: flex;
    align-items: center;
    justify-content: center;
    gap: 18px;
  }
  .front-brand__square {
    width: 54px; height: 54px;
    background: var(--emboss);
  }
  .front-brand__name {
    font-weight: 700;
    font-size: 50px;
    letter-spacing: 1px;
    color: var(--emboss);
  }

  /* Back */
  .band-cyan {
    position: absolute; left: 0; top: 0; bottom: 0;
    width: 40px; background: var(--brand-cyan);
  }
  .band-light {
    position: absolute; left: 40px; top: 0; bottom: 0;
    width: 9px; background: var(--stripe-light);
  }
  .person { position: absolute; left: 86px; top: 46px; }
  .person__name {
    font-weight: 700; font-size: 22px; color: var(--brand-cyan);
  }
  .person__title {
    font-size: 13px; line-height: 17px; color: var(--ink-white); margin-top: 4px;
  }
  .company {
    position: absolute; left: 86px; top: 160px;
    font-weight: 700; font-size: 19px; color: var(--brand-cyan);
  }
  .contacts {
    position: absolute; left: 86px; top: 196px;
    list-style: none;
    font-size: 14px; line-height: 20px; color: var(--ink-white);
  }
  .contacts li { display: flex; align-items: center; gap: 8px; }
  .contacts svg { width: 12px; height: 12px; fill: var(--brand-cyan); flex: none; }
  .contacts .label { color: var(--brand-cyan); }
  .address {
    position: absolute; left: 86px; top: 300px;
    font-size: 14px; color: var(--ink-white);
  }
  .back-brand {
    position: absolute; right: 40px; top: 168px;
    display: flex; align-items: center; gap: 10px;
  }
  .back-brand__square { width: 26px; height: 26px; background: var(--mark-silver); }
  .back-brand__name {
    font-weight: 700; font-size: 22px; color: var(--mark-silver); letter-spacing: 0.5px;
  }
</style>
</head>
<body>

<section class="card card--front" aria-label="Card front">
  <div class="front-brand">
    <span class="front-brand__square"></span>
    <span class="front-brand__name">TOVAR CREST</span>
  </div>
</section>

<section class="card card--back" aria-label="Card back">
  <div class="band-cyan"></div>
  <div class="band-light"></div>

  <div class="person">
    <h1 class="person__name">Carla Beth Soren</h1>
    <p class="person__title">Vice President,<br>APAC M&amp;A Operations</p>
  </div>

  <h2 class="company">Tovar Crest Asia Pacific Limited</h2>

  <ul class="contacts">
    <li>
      <svg viewBox="0 0 12 12" aria-hidden="true"><rect x="3" y="0.5" width="6" height="11" rx="1.2"/></svg>
      +852 6481 2037
    </li>
    <li>
      <svg viewBox="0 0 12 12" aria-hidden="true"><path d="M2.5 1l2 0 1 3-1.3 1a6.5 6.5 0 0 0 2.8 2.8l1-1.3 3 1v2c0 .8-.6 1.3-1.4 1.3A9.5 9.5 0 0 1 1.2 2.4C1.2 1.6 1.7 1 2.5 1z"/></svg>
      +852 2736 4100
    </li>
    <li>
      <svg viewBox="0 0 12 12" aria-hidden="true"><rect x="3" y="0.5" width="6" height="3"/><rect x="0.5" y="4" width="11" height="5" rx="1"/><rect x="3" y="8" width="6" height="3.5"/></svg>
      +852 2736 4155,&nbsp;<span class="label">VOIP:</span>&nbsp;4813
    </li>
    <li>
      <svg viewBox="0 0 12 12" aria-hidden="true"><path d="M0.5 2.5h11v7h-11z M0.5 2.5l5.5 4 5.5-4"/></svg>
      cbsoren@tovarcrest.com
    </li>
  </ul>

  <p class="address">Unit 1407, K82, 27 Sai Lok Fung Road, Hong Kong</p>

  <div class="back-brand">
    <span class="back-brand__square"></span>
    <span class="back-brand__name">TOVAR CREST</span>
  </div>
</section>

</body>
</html>
```